Business Card Design - Service Company

Use of the card mainly in living rooms and relations b2b We wish a card with a modern design, blue tones in the background would be a plus The card must be front / back (one side with the logo / the other with the information of contact )

Font styles to use
Serif

Requirements
Must have
• Using the map on the back of the business card Editable format! Photoshop CS2 / Illustrator CS2
Nice to have
• Maquis Vertex IT Pierre Blanche Commercial Center, 20480 Lorvanu 0495718243 Siret 71384096200018 APE 6203Y https://www.fb.com/ateliertech.maquisvertex www.maquis-vertex.com

```html
<!DOCTYPE html>
<html lang="fr">
<head>
<meta charset="utf-8">
<title>Maquis Vertex IT – Carte de visite</title>
<link href="https://fonts.googleapis.com/css2?family=Lato:wght@400;700;900&display=swap" rel="stylesheet">
<style>
  :root{
    --page:#cfe5ec;
    --card:#dcedf3;
    --card-back:#e4f0f4;
    --map-light:#d3e3e8;
    --map-dark:#bcd3da;
    --blue:#1f86d1;
    --blue-band:#2a8bcc;
    --ink:#2a2c2e;
    --grey:#6f7376;
    --white:#ffffff;
  }
  *{margin:0;padding:0;box-sizing:border-box}
  html,body{width:1200px;height:835px;overflow:hidden}
  body{background:var(--page);font-family:"Lato",sans-serif;position:relative}

  .card{position:absolute;top:262px;width:540px;height:312px;overflow:hidden;
        box-shadow:0 8px 24px rgba(40,90,110,.18)}

  /* logo side */
  .card--brand{left:36px;background:var(--card-back)}
  .brand__map{position:absolute;left:0;top:0;width:100%;height:234px;
        background:radial-gradient(ellipse at 45% 45%,var(--map-dark),var(--map-light) 70%)}
  .brand__rule{position:absolute;left:0;top:120px;width:300px;height:2px;background:var(--blue)}
  .brand__name{position:absolute;left:316px;top:104px;font-weight:900;font-size:26px;
        color:var(--blue);letter-spacing:.5px;line-height:32px}
  .brand__band{position:absolute;left:0;bottom:0;width:100%;height:78px;background:var(--blue-band);
        display:flex;align-items:center;padding-left:56px;gap:16px;color:var(--white);font-size:15px;letter-spacing:.4px}
  .brand__dot{width:26px;height:26px;border-radius:50%;background:var(--white);flex:none}

  /* contact side */
  .card--contact{left:624px;background:var(--card)}
  .contact__title{position:absolute;left:30px;top:56px;font-weight:900;font-size:24px;color:var(--ink);letter-spacing:.6px}
  .contact__rule{position:absolute;height:2px;background:var(--blue)}
  .contact__rule--top{left:248px;top:100px;right:0}
  .contact__rule--bottom{left:30px;top:262px;width:280px}
  .contact__logo{position:absolute;right:30px;top:56px;font-weight:900;font-size:22px;color:var(--blue);letter-spacing:.4px}
  .contact__item{position:absolute;display:flex;flex-direction:column;align-items:center;gap:14px;
        font-size:14px;color:var(--ink);text-align:center;line-height:19px;letter-spacing:.3px}
  .contact__item--web{left:20px;top:128px;width:170px}
  .contact__item--phone{left:190px;top:128px;width:150px}
  .contact__item--address{left:340px;top:128px;width:196px}
  .icon{width:40px;height:40px;border-radius:50%;background:var(--blue);display:flex;align-items:center;justify-content:center}
  .icon svg{width:22px;height:22px;fill:none;stroke:var(--white);stroke-width:1.6;stroke-linecap:round;stroke-linejoin:round}
  .contact__legal{position:absolute;left:30px;top:238px;font-size:14px;font-weight:700;color:var(--blue);letter-spacing:.4px}
</style>
</head>
<body>

<section class="card card--brand" aria-label="Recto">
  <div class="brand__map" role="img" aria-label="Carte du monde pâle avec points d'implantation en Amérique du Nord"></div>
  <div class="brand__rule"></div>
  <div class="brand__name">Maquis Vertex IT</div>
  <div class="brand__band">
    <span class="brand__dot"></span>
    <span>https://www.fb.com/ateliertech.maquisvertex</span>
  </div>
</section>

<section class="card card--contact" aria-label="Verso">
  <h1 class="contact__title">Maquis Vertex IT</h1>
  <div class="contact__logo">Maquis Vertex IT</div>
  <div class="contact__rule contact__rule--top"></div>

  <div class="contact__item contact__item--web">
    <span class="icon"><svg viewBox="0 0 24 24"><rect x="3" y="6" width="18" height="12" rx="1"/><path d="M3 7l9 6 9-6"/></svg></span>
    <span>www.maquis-vertex.com</span>
  </div>
  <div class="contact__item contact__item--phone">
    <span class="icon"><svg viewBox="0 0 24 24"><path d="M7 3h3l1.5 4-2 1.5a11 11 0 0 0 6 6l1.5-2 4 1.5v3a2 2 0 0 1-2 2A16 16 0 0 1 5 5a2 2 0 0 1 2-2z"/></svg></span>
    <span>0495718243</span>
  </div>
  <div class="contact__item contact__item--address">
    <span class="icon"><svg viewBox="0 0 24 24"><path d="M10 14a4 4 0 0 0 5.6 0l3-3a4 4 0 0 0-5.6-5.6l-1 1"/><path d="M14 10a4 4 0 0 0-5.6 0l-3 3a4 4 0 0 0 5.6 5.6l1-1"/></svg></span>
    <span>Centre Commercial<br>Pierre Blanche, 20480 Lorvanu</span>
  </div>

  <p class="contact__legal">Siret 71384096200018 APE 6203Y</p>
  <div class="contact__rule contact__rule--bottom"></div>
</section>

</body>
</html>
```